School annual plan - describing all our goals for 2026

This is a high school plan. The design should be similar in style to other school flyers and posters.

2026 Tallow SHS AIP - the document to design. Please make 1 page.

Documents to follow style:
Document 1: the 2025 School Annual Plan (use this for formatting. Change style to similar to Documents 2 & 3).

Document 2: the Tallow Instructional Model - make the style similar to this.

Document 3: Explicit Instruction Classroom Matrix - Another document to make the style similar to.

This is the school's website: https://tallowshs.qz.edu.au/

Please let me know if you have any questions.

```html
<!DOCTYPE html>
<html lang="en">
<head>
<meta charset="utf-8">
<title>Tallow SHS – 2026 Annual Implementation Plan</title>
<link href="https://fonts.googleapis.com/css2?family=Montserrat:wght@800;900&family=Arimo:wght@400;700&display=swap" rel="stylesheet">
<style>
:root{
  --navy:#1a3e8c;
  --yellow:#f3e46b;
  --sky:#29a9e0;
  --orange:#e89a2f;
  --pale:#7db7e3;
  --wash:#e0ecf9;
  --rule:#a9b3c2;
  --ink:#1f1f1f;
  --backdrop:#d9dce1;
  --paper:#ffffff;
}
*{box-sizing:border-box;margin:0;padding:0}
html,body{width:1200px;height:998px;overflow:hidden}
body{background:var(--backdrop);font-family:"Arimo",Arial,sans-serif;color:var(--ink);font-size:8px;line-height:1.22}
.poster{position:absolute;left:14px;top:26px;width:1172px;height:946px;background:var(--paper);padding:12px;box-shadow:0 2px 8px rgba(0,0,0,.18)}
.frame{border:2px solid var(--navy);height:100%;display:flex;flex-direction:column}
.masthead{background:var(--navy);height:126px;display:flex;align-items:center;padding:0 34px 0 38px;gap:40px}
.school-mark{width:140px;display:flex;align-items:center;gap:8px;color:#fff;font-family:"Montserrat",sans-serif;font-weight:800;font-size:17px}
.school-mark .dot{width:22px;height:22px;border-radius:50%;background:var(--yellow);flex:none}
.titles{flex:1}
.title-main{font-family:"Montserrat",sans-serif;font-weight:900;color:#fff;font-size:40px;letter-spacing:7.5px;line-height:1;white-space:nowrap}
.title-rule{height:3px;background:var(--yellow);margin:9px 0 8px}
.title-sub{font-family:"Montserrat",sans-serif;font-weight:900;color:var(--yellow);font-size:33px;letter-spacing:6.2px;line-height:1;white-space:nowrap}
.body{flex:1;padding:12px 6px 6px;display:flex;flex-direction:column;gap:7px}
.priorities{display:flex;gap:7px}
.priority{flex:1;display:grid;grid-template-columns:92px 1fr 196px;border:2px solid var(--rule)}
.label{background:var(--navy);color:#fff;font-weight:700;font-size:11px;line-height:1.25;padding:8px 9px;border-bottom:1px solid var(--rule)}
.priority-title{padding:6px 10px;font-weight:700;font-size:9.5px;line-height:1.3;border-bottom:1px solid var(--rule)}
.monitoring{border-left:1px solid var(--rule);border-bottom:1px solid var(--rule);display:flex;flex-direction:column}
.monitoring h4{color:var(--navy);font-size:10.5px;text-align:center;padding:5px 0 4px;border-bottom:1px solid var(--rule)}
.terms{display:flex;flex:1}
.terms span{flex:1;color:#fff;font-size:7.5px;display:flex;align-items:center;justify-content:center}
.t1{background:var(--navy)}.t2{background:var(--sky)}.t3{background:var(--orange)}.t4{background:var(--pale)}
.cell{grid-column:2/4;padding:7px 10px;border-bottom:1px solid var(--rule)}
.focus-head{color:var(--navy);font-weight:700;font-size:11px;margin-bottom:2px}
ul{list-style:disc;padding-left:10px}
li{margin-bottom:1.6px}
.two-col{columns:2;column-gap:30px}
.actions{grid-column:1/4;background:var(--wash);display:flex;padding:8px 10px 6px 14px;gap:12px}
.actions-list{flex:1}
.resources{width:196px;border-left:1.5px solid var(--navy);padding-left:10px}
.block-head{color:var(--navy);font-weight:700;font-size:11px;margin-bottom:2px}
.block-head small{font-size:8.5px}
.criteria{display:grid;grid-template-columns:22px 24px 1fr;border:2px solid var(--rule)}
.strip-navy{background:var(--navy);grid-row:1/4;display:flex;align-items:center;justify-content:center}
.strip-yellow{background:var(--yellow);display:flex;align-items:center;justify-content:center;border-bottom:1px solid var(--rule)}
.vertical{writing-mode:vertical-rl;transform:rotate(180deg);font-weight:700;font-size:10px;white-space:nowrap}
.strip-navy .vertical{color:#fff}
.strip-yellow .vertical{color:var(--navy)}
.measures-yellow{grid-row:1/3}
.row{display:grid;grid-template-columns:30fr 19fr 36fr 15fr;border-bottom:1px solid var(--rule);grid-column:3}
.row>div{padding:7px 10px 6px 14px}
.row .sub-head{color:var(--navy);font-weight:700;font-size:8.5px;margin-bottom:2px}
.row .perf-head{color:var(--navy);font-weight:700;font-size:9.5px;line-height:1.3;margin-bottom:2px}
.artefacts{display:grid;grid-template-columns:30fr 70fr;grid-column:3}
.artefacts>div{padding:7px 10px 6px 14px}
.artefacts>div+div{border-left:1px solid var(--rule)}
.redtape{border:2px solid var(--rule);padding:6px 8px}
.redtape h3{color:var(--navy);font-size:11px;margin-bottom:2px}
.redtape-cols{display:flex;gap:30px}
.redtape-cols ul{width:300px}
</style>
</head>
<body>
<main class="poster">
 <div class="frame">
  <header class="masthead">
   <div class="school-mark"><span class="dot"></span>Tallow SHS</div>
   <div class="titles">
    <h1 class="title-main">TALLOW STATE HIGH SCHOOL</h1>
    <div class="title-rule"></div>
    <h2 class="title-sub">2026 ANNUAL IMPLEMENTATION PLAN</h2>
   </div>
  </header>

  <div class="body">
   <section class="priorities">
    <article class="priority">
     <div class="label">School<br>priority 1</div>
     <div class="priority-title">Belonging and Engagement<br>In classrooms: Pedagogy-whole school focus on pedagogy and “How Tallow Students Learn”</div>
     <div class="monitoring"><h4>MONITORING</h4><div class="terms"><span class="t1">Term 1</span><span class="t2">Term 2</span><span class="t3">Term 3</span><span class="t4">Term 4</span></div></div>
     <div class="label">Link to school improvement strategy:</div>
     <div class="cell">
      <p class="focus-head">Our 2026 focus area for improvement is to:</p>
      <ul>
       <li>Enact planned and intentional pedagogical practices that align to How Tallow Students Learn</li>
       <li>Conduct regular in-class observation and feedback cycles</li>
       <li>Deliver intensive pedagogy support for teachers using classroom profiling, walkthroughs and structured feedback in explicit instruction pedagogy</li>
       <li>Adopt clear processes to track, monitor and differentiate support so that every child is learning and improving</li>
       <li>Drive Digital Innovation through the integration of ZLearn.</li>
      </ul>
     </div>
     <div class="label">Strategies</div>
     <div class="cell">
      <ul>
       <li>Line Management, quality assurance, setting professional goals (SPG)</li>
       <li>Observation and Feedback Framework</li>
       <li>Classroom Profiling</li>
       <li>Differentiated approaches to pedagogy</li>
       <li>Digital Pedagogy</li>
      </ul>
     </div>
     <div class="actions">
      <div class="actions-list">
       <p class="block-head">Actions: <small>including Responsible role(s)</small></p>
       <ul>
        <li>Visible, planned and intentional pedagogical practices in all learning environments</li>
        <li>Quality assurance, line of sight, professional learning, meetings, classrooms, feedback</li>
        <li>Continue to embed ZLearn as the core platform for curriculum programs, and resources</li>
        <li>Enact professional development for pedagogical practices, classroom profiling and digital learning for all staff</li>
        <li>100% of teachers engaged in at least one Observation &amp; Feedback cycle per semester</li>
        <li>Continue “How Tallow Students Learn”</li>
        <li>Every teacher being observed through walkthroughs from leadership.</li>
       </ul>
      </div>
      <div class="resources">
       <p class="block-head">Resources</p>
       <ul>
        <li>Tallow HITS</li>
        <li>Critical Routines</li>
        <li>ESCMs</li>
        <li>How Tallow Students Learn</li>
        <li>Classroom Observation &amp; Feedback Cycle</li>
        <li>MTSS documents</li>
       </ul>
      </div>
     </div>
    </article>

    <article class="priority">
     <div class="label">School<br>priority 2</div>
     <div class="priority-title" style="padding-top:11px">Curriculum- Continued improvement<br>Year 7-12 curriculum</div>
     <div class="monitoring"><h4>MONITORING</h4><div class="terms"><span class="t1">Term 1</span><span class="t2">Term 2</span><span class="t3">Term 3</span><span class="t4">Term 4</span></div></div>
     <div class="label">Link to school improvement strategy:</div>
     <div class="cell">
      <p class="focus-head">Our 2026 focus area for improvement is to:</p>
      <ul>
       <li>Deliver an aligned and engaging curriculum that is regularly reviewed as part of a quality assurance cycle</li>
       <li>Enact a Whole-School Moderation Policy ensuring alignment, validity, and reliability of teacher judgments: before, after, end</li>
       <li>Deepen the school’s Reading Strategy under MTSS, targeting Tier 1, 2, and 3 interventions</li>
       <li>Complete full alignment to Australian Curriculum V9, ensuring consistency across Years 7–10</li>
       <li>Strengthen QCE attainment and pathways monitoring for Years 10–12 students.</li>
      </ul>
     </div>
     <div class="label">Strategies</div>
     <div class="cell">
      <ul class="two-col">
       <li>Teaching and Learning- all HoD aligned</li>
       <li>Line Management- quality assurance</li>
       <li>Whole school walk-throughs</li>
       <li>Moderation- before, after, end</li>
       <li>Whole School Reading Strategy</li>
       <li>V9 Australian Curriculum with accessible assessment</li>
       <li>Maximising Learning Team and collaboration time</li>
       <li>Widen VET options in Senior School</li>
       <li>Senior School Pathways document.</li>
      </ul>
     </div>
     <div class="actions">
      <div class="actions-list">
       <p class="block-head">Actions: <small>including Responsible role(s)</small></p>
       <ul>
        <li>Continue to embed ZLearn as the core platform for curriculum programs, and resources in Year 7 &amp; 8 Core, VET and Year 11 &amp; 12 for assessment submission</li>
        <li>Continue implementation of Australian Curriculum V9</li>
        <li>Continue to deliver 2024 QSCA Applied syllabuses and 2025 QSCA General syllabuses</li>
        <li>Increase VET options to meet the needs of our learners, priority in Year 10 2026</li>
        <li>Enact differentiated curriculum that meets the individual needs of students in classrooms</li>
       </ul>
      </div>
      <div class="resources">
       <p class="block-head">Resources</p>
       <ul>
        <li>ZLearn</li>
        <li>MeetHub</li>
        <li>Data Plan</li>
        <li>Learn Ahead CURA</li>
        <li>QSCA</li>
        <li>CARF- K-12 Framework</li>
        <li>DoE Curriculum Portal</li>
        <li>Skills.gov</li>
       </ul>
      </div>
     </div>
    </article>
   </section>

   <section class="criteria">
    <div class="strip-navy"><span class="vertical">End of Year Success Criteria</span></div>
    <div class="strip-yellow measures-yellow"><span class="vertical">Measures</span></div>
    <div class="row">
     <div>
      <p class="perf-head">Performance:<br>AIP measurable/desired outcomes engagement:</p>
      <ul>
       <li>10% Reduction in behaviour incidents</li>
       <li>8% SDA rate- whole school</li>
       <li>90% Attendance</li>
       <li>Improved student retention</li>
       <li>VET- 100% CERT II</li>
       <li>Out of Catchment enrolments &lt;20% (24% in 2025)</li>
      </ul>
     </div>
     <div>
      <p class="sub-head">AIP measurable/desired outcomes engagement:</p>
      <ul>
       <li>10% Reduction in behaviour incidents</li>
       <li>8% SDA rate- whole school</li>
       <li>90% Attendance</li>
       <li>Improved student retention</li>
       <li>VET- 100% CERT II</li>
       <li>Out of Catchment enrolments &lt;20% (24% in 2025)</li>
      </ul>
     </div>
     <div>
      <p class="sub-head">AIP measurable/desired outcomes engagement:</p>
      <ul>
       <li>Increase in proportion of students achieving a C &amp; above in all subjects with a focus on English and Maths</li>
       <li>Increase in proportion of students achieving an A or B in all subjects with a focus on English and Maths</li>
       <li>Maintain 100% of students achieving a QCE/ QCIA</li>
       <li>Improved rates of student attendance- days of learning</li>
       <li>Reduction in school disciplinary absence rates</li>
       <li>Improved Year 13 Next Steps Results</li>
       <li>Improved First Nations Outcomes- Closing the Gap- attendance &amp; academic outcomes</li>
       <li>Improved participation and performance in NAPLAN</li>
      </ul>
     </div>
     <div>
      <p class="sub-head">AIP measurable/desired outcomes performance (whole school):</p>
      <ul>
       <li>45% A-B</li>
       <li>90% A-C</li>
       <li>100% A-D</li>
       <li>100% QCE/QCIA (Year 12 2026)</li>
      </ul>
     </div>
    </div>
    <div class="row">
     <div>
      <p class="sub-head">Behaviour Staff will:</p>
      <ul>
       <li>Apply the Critical Routines, Essential Skills for Classroom Management &amp; How Tallow Students Learn</li>
       <li>Access agreed data sets to know their learners, plan &amp; differentiate to ensure accessibility for all students</li>
       <li>Use Multi Tiered Systems of Support and the Student Referral Team to support behaviour, academics, and wellbeing to improve outcomes for students</li>
       <li>Utilise ZLearn for all 7, 8, Senior School Submissions &amp; VET classes from 2026</li>
      </ul>
     </div>
     <div>
      <p class="sub-head">Students will:</p>
      <ul>
       <li>Be prepared and ready for learning &amp; follow Critical Routines</li>
       <li>Know, <b>what, how</b> &amp; <b>why</b> they are learning</li>
      </ul>
     </div>
     <div>
      <p class="sub-head">Education Support Officers will:</p>
      <ul>
       <li>Maximise their time in classrooms with students- face to face</li>
       <li>Support the students in classrooms, in year level hubs, in the reset room and in alternative learning environments.</li>
      </ul>
     </div>
     <div>
      <p class="sub-head">Leadership Team will:</p>
      <ul>
       <li>Support all teaching and non- teaching staff</li>
       <li>Demonstrate Instructional Leadership</li>
       <li>Display visible leadership in the classroom/s.</li>
      </ul>
     </div>
    </div>
    <div class="strip-yellow" style="border-bottom:0"><span class="vertical">Artefacts</span></div>
    <div class="artefacts">
     <div>
      <ul>
       <li>Moderation Plan- Before, After, End, including a HOD planned collaboration cycle</li>
       <li>Staff Collaborative Planning Outcomes</li>
       <li>Three Levels of Planning</li>
       <li>Curriculum Aligned Marking Guides</li>
      </ul>
     </div>
     <div>
      <ul>
       <li>ZLearn - Resourcing and Unit Plans</li>
       <li>AARAs</li>
       <li>Assessment Calendar</li>
       <li>Maximising Learning Team Outcomes</li>
      </ul>
     </div>
    </div>
   </section>

   <section class="redtape">
    <h3>Reduction of red tape in day-to-day work, planning and processes include:</h3>
    <div class="redtape-cols">
     <ul>
      <li>Tallow Strategy – Ask: Is this the best way to do it? How do we keep it simple?</li>
      <li>Strategic Meeting Scheduling</li>
      <li>Investigate assessment submission</li>
     </ul>
     <ul style="width:400px">
      <li>NCCD data collection to be reviewed</li>
      <li>Increase use of Learn Ahead- for student work at home requirements</li>
     </ul>
    </div>
   </section>
  </div>
 </div>
</main>
</body>
</html>
```